I need a new business card design for my pharmacy.

I need a business card design. I will include my logo.
The card needs to be readable. I prefer to have my logo on one side along with my website, the other side includes the other information. Please use combination of black, neon green, white, and silver. This needs to catch the eye but yet be clearly visible and legible. Thanks

Industry/Entity Type

Pharmacy

Contact Information for Business Card

It needs to have the following information listed:
Mel's Apothecary Owner/Pharm D.
7134 North Brook Lane
Sioux Falls, SD 57231
Phone 605-318-6207
Fax 605-318-6209
email: mel@melsapothecary-example.com
www.melsapothecary-example.com
Store hours Monday-Friday 8 am- 7 pm
Saturday 8 am- 12 pm
Sunday Closed
Please utilize the colors black, white, and neon green, maybe silver.

Requirements
Must have
• It needs to be easily readable!
Nice to have
• It should catch the eye.
Should not have
• Do not use any other colors except listed: black, neon green, white, & silver.

```html
<!DOCTYPE html>
<html lang="en">
<head>
<meta charset="utf-8">
<title>Mel's Apothecary – Business Card</title>
<link rel="stylesheet" href="https://fonts.googleapis.com/css2?family=Source+Sans+3:wght@400;600;700&display=swap">
<style>
  :root {
    --ink: #050505;
    --neon: #a6cc3a;
    --white: #ffffff;
    --backdrop: #ece8e0;
  }
  * { margin: 0; padding: 0; box-sizing: border-box; }
  html, body {
    width: 1046px; height: 1200px; overflow: hidden;
    background: var(--backdrop);
    font-family: "Source Sans 3", "Segoe UI", sans-serif;
  }
  .canvas { position: relative; width: 1046px; height: 1200px; }
  .card {
    position: absolute; left: 105px; width: 822px; height: 470px;
    background: var(--ink); color: var(--white);
  }
  .card--front { top: 81px; }
  .card--back { top: 642px; }

  /* front */
  .brand {
    position: absolute; left: 0; right: 0; top: 231px;
    transform: translateY(-50%);
    display: flex; align-items: center; justify-content: center; gap: 26px;
  }
  .brand__dot { width: 46px; height: 46px; border-radius: 50%; background: var(--neon); }
  .brand__name {
    font-size: 64px; font-weight: 600; letter-spacing: -1.5px; color: var(--white);
    line-height: 1;
  }
  .website {
    position: absolute; left: 0; right: 0; top: 412px;
    text-align: center; font-size: 29px; color: var(--neon); line-height: 1.2;
  }

  /* back */
  .owner { position: absolute; left: 53px; top: 26px; display: inline-block; }
  .owner__title { font-size: 38px; font-weight: 700; line-height: 1.1; letter-spacing: 0.2px; }
  .owner__degree {
    display: block; text-align: right; color: var(--neon);
    font-size: 21px; font-weight: 700; line-height: 1; margin-top: 2px;
  }
  .contacts { position: absolute; left: 53px; top: 172px; font-size: 22px; line-height: 36px; }
  .contacts__row { display: flex; }
  .contacts__label { width: 117px; }

  .band-line { position: absolute; left: 0; width: 100%; height: 8px; background: var(--neon); }
  .band-line--top { top: 310px; }
  .band-line--bottom { top: 438px; }
  .band {
    position: absolute; left: 0; top: 322px; width: 100%; height: 112px;
    background: var(--neon); color: var(--ink);
    font-size: 22px; line-height: 29.5px;
  }
  .band__address { position: absolute; left: 53px; top: 12px; }
  .band__hours { position: absolute; left: 479px; top: 12px; }
</style>
</head>
<body>
<main class="canvas">
  <section class="card card--front" aria-label="Card front">
    <div class="brand">
      <span class="brand__dot"></span>
      <span class="brand__name">Mel's Apothecary</span>
    </div>
    <p class="website">www.melsapothecary-example.com</p>
  </section>

  <section class="card card--back" aria-label="Card back">
    <div class="owner">
      <h1 class="owner__title">Mel's Apothecary Owner</h1>
      <span class="owner__degree">Pharm D.</span>
    </div>
    <div class="contacts">
      <p class="contacts__row"><span class="contacts__label">Phone</span><span>: 605-318-6207</span></p>
      <p class="contacts__row"><span class="contacts__label">Fax</span><span>: 605-318-6209</span></p>
      <p class="contacts__row"><span class="contacts__label">Email</span><span>: mel@melsapothecary-example.com</span></p>
    </div>
    <div class="band-line band-line--top"></div>
    <div class="band">
      <p class="band__address">7134 North Brook Lane<br>Sioux Falls,<br>SD 57231</p>
      <p class="band__hours">Monday-Friday 8 am- 7 pm<br>Saturday 8 am- 12 pm<br>Sunday Closed</p>
    </div>
    <div class="band-line band-line--bottom"></div>
  </section>
</main>
</body>
</html>
```